CoralPeak Holdings Inc. Business Card Design

My business is custom renovations and homes.I would need to have a new business logo created to go along with my company name. The business card should be of a modern style as this is the market I am focused on. I would need my contact information and website posted on the card. I would also like to list a few of the tasks I conduct on the card (such as: Renovations, Additions, Repairs, New Homes, Design, Consultations). On the reverse of the card I currently have just my logo and my motto, "Crafting A Bold Dawn". However, I am open to completely changing everything as I am starting a new year and would like to excel further. Any new ideas and suggestions are always welcomed. Thank you.

Target Market(s)

Upscale residential and commercial renovations and builds

Industry/Entity Type

Business

Contact Information for Business Card

I would like the design to be able to be laser cut or burnt onto a wooden business card. I will be creating one option of cards for really loyal customers (wooden) and a second option for the everyday customer (paper).

Font styles to use
Other font styles liked:
• Calibri / anything of mordern taste

Colors
f37122
5c5c5c
474747
ffffff

Requirements
Must have
• I would like the colours of my business to be a sharp orange and grey. I believe this will symbolize a modern style. I am open to other suggestions if this is not suitable for the designers tastes. My contact info as follows:
• Jack Merlin
• President
• CoralPeak Holdings Inc.
• 555-392-7184
• jack@coralpeakholdings.example
• I would like my website (currently under construction) coralpeakholdings.example on the card aswell.
Nice to have
• Along with a modern logo representing CoralPeak, I would like something on the card besides the logo and contact information. Perhaps a small background design. I feel it may be nice to have my services listed on the card (in smaller font on the bottom) Renovations, Additions, Repairs, Design, Consultations.
Should not have
• The business card should not have too many different colors. Should not have rounded corners.

```html
<!DOCTYPE html>
<html lang="en">
<head>
<meta charset="utf-8">
<title>CoralPeak Holdings Inc. – Business Card</title>
<link href="https://fonts.googleapis.com/css2?family=Roboto:wght@400;500;700&display=swap" rel="stylesheet">
<style>
  :root {
    --orange: #f37122;
    --grey: #5c5c5c;
    --grey-dark: #474747;
    --card: #1f1f21;
    --card-back: #18181a;
    --white: #ffffff;
    --stage: #2e2a28;
  }
  * { box-sizing: border-box; margin: 0; padding: 0; }
  html, body {
    width: 1200px; height: 716px; overflow: hidden;
    background: var(--stage);
    font-family: "Roboto", Arial, sans-serif;
    color: var(--white);
  }
  .stage {
    position: relative; width: 1200px; height: 716px;
    display: flex; align-items: center; justify-content: center; gap: 60px;
  }
  .card {
    position: relative; width: 520px; height: 297px; overflow: hidden;
    background: var(--card);
    box-shadow: 0 10px 30px rgba(0,0,0,.45);
  }
  /* Back */
  .card--back { background: var(--card-back); display: flex; align-items: center; justify-content: center; }
  .card--back .back-name { font-size: 46px; font-weight: 700; color: var(--grey); letter-spacing: .5px; }

  /* Front */
  .brand { position: absolute; left: 34px; top: 34px; display: flex; align-items: center; gap: 12px; }
  .brand-square { width: 34px; height: 34px; background: var(--orange); }
  .brand-name { font-size: 24px; font-weight: 700; color: var(--orange); line-height: 1; }
  .brand-sub { font-size: 17px; font-weight: 400; color: var(--white); margin-top: 3px; }
  .divider { position: absolute; left: 34px; right: 34px; top: 112px; height: 1px; background: var(--grey); }

  .services { position: absolute; left: 34px; top: 132px; list-style: none; font-size: 12.5px; line-height: 17px; }
  .services li::before { content: "»"; color: var(--orange); margin-right: 6px; }
  .services .inline::before { content: none; }
  .services .inline .sep { color: var(--orange); margin: 0 5px; }

  .person { position: absolute; right: 34px; top: 128px; text-align: right; }
  .person-name { font-size: 21px; font-weight: 700; color: var(--orange); letter-spacing: .5px; }
  .person-title { font-size: 12.5px; margin-top: 4px; padding-top: 3px; border-top: 1px solid var(--grey); display: inline-block; padding-left: 30px; }

  .contacts { position: absolute; right: 34px; top: 188px; list-style: none; font-size: 12.5px; line-height: 20px; text-align: right; }
  .contacts li { display: flex; align-items: center; justify-content: flex-end; gap: 8px; }
  .contacts svg { width: 13px; height: 13px; fill: var(--orange); }

  .bands { position: absolute; left: 0; bottom: 0; width: 520px; height: 46px; }
  .website { position: absolute; right: 34px; bottom: 13px; font-size: 14px; font-weight: 500; color: var(--white); }
</style>
</head>
<body>
<main class="stage">
  <section class="card card--back" aria-label="Card back">
    <span class="back-name">CoralPeak</span>
  </section>

  <section class="card card--front" aria-label="Card front">
    <div class="brand">
      <span class="brand-square"></span>
      <div>
        <div class="brand-name">CoralPeak</div>
        <div class="brand-sub">Holdings Inc.</div>
      </div>
    </div>
    <div class="divider"></div>

    <ul class="services">
      <li>Additions</li>
      <li>Renovations</li>
      <li>Consultations</li>
      <li>Repairs<span class="sep" style="color:var(--orange);margin:0 5px">»</span>Design</li>
    </ul>

    <div class="person">
      <div class="person-name">Jack Merlin</div>
      <div class="person-title">President</div>
    </div>

    <ul class="contacts">
      <li>555-392-7184
        <svg viewBox="0 0 24 24" aria-hidden="true"><path d="M6.6 10.8a15 15 0 0 0 6.6 6.6l2.2-2.2a1 1 0 0 1 1-.25 11.4 11.4 0 0 0 3.6.57 1 1 0 0 1 1 1V20a1 1 0 0 1-1 1A17 17 0 0 1 3 4a1 1 0 0 1 1-1h3.5a1 1 0 0 1 1 1c0 1.25.2 2.45.57 3.57a1 1 0 0 1-.25 1z"/></svg>
      </li>
      <li>jack@coralpeakholdings.example
        <svg viewBox="0 0 24 24" aria-hidden="true"><path d="M2 5h20v14H2z M2 5l10 8 10-8" fill="none" stroke="#f37122" stroke-width="2"/></svg>
      </li>
    </ul>

    <svg class="bands" viewBox="0 0 520 46" preserveAspectRatio="none" aria-hidden="true">
      <rect x="0" y="10" width="520" height="36" fill="#474747"/>
      <polygon points="250,0 520,0 520,46 220,46" fill="#f37122"/>
    </svg>
    <span class="website">www.coralpeakholdings.example</span>
  </section>
</main>
</body>
</html>
```